Glimmerseal pond linings website template

We need a template for our new website. Glimmerseal is currently marketed through www.tarpavale.com.au, and we are moving the pond/dam linings to a dedicated site www.glimmerseal.com.au

The site is essentially brochureware. The content (less landing page & photo gallery) is on the new site to give you a better idea of what we do. We are also on Facebook.com/glimmerseal

We are looking for a template/style which we can adapt to the different sections of the site as required. We also get a lot of phone/tablet visitors so an alternative mobile layout would be a bonus, but by no means required.

I am proficient in HTML/CSS & javascript so can code most designs thrown at me.

Any icons or interface fonts should be freely available web fonts where possible.

Target Market(s)

We are targeting both landscape professionals (design & construction) as well as the DIY market for ponds/wateragrdens.

Industry/Entity Type

Moving

Requirements
Must have
• We need a design (preferably layered PSD or AI) as basis for our overall site look and feel. Fonts/iconography/layout are where we are lacking. We can do the HTML/CSS/JS/PHP internally.
Nice to have
• A style guide either in file or separate would be nice.
Layers with effect (i.e.. :hover, CSS3 transition endpoints, etc)

```html
<!DOCTYPE html>
<html lang="en">
<head>
<meta charset="utf-8">
<title>Glimmerseal — Custom made liners</title>
<link href="https://fonts.googleapis.com/css2?family=Noto+Serif:ital,wght@0,400;0,700;1,400&family=Ubuntu:wght@400;500;700&family=Open+Sans:wght@400;600&display=swap" rel="stylesheet">
<style>
:root{
  --green:#8cbf26;
  --green-dark:#1e7a3c;
  --caption:#6a9e2a;
  --ink:#333;
  --muted:#999;
  --link:#1a8fc9;
  --rule:#dcdcdc;
  --wood-top:#f9dcc6;
  --wood-bottom:#f5cfb2;
  --header-top:#fdf6f0;
  --header-bottom:#f9e9dc;
  --page:#fafafa;
  --footer:#ececec;
  --serif:"Noto Serif",Georgia,serif;
  --sans:"Open Sans",Arial,sans-serif;
  --display:"Ubuntu",Arial,sans-serif;
}
*{box-sizing:border-box;margin:0;padding:0}
html,body{width:932px;height:1200px;overflow:hidden}
body{background:var(--page);font-family:var(--sans);color:var(--ink);position:relative}

.site-header{position:absolute;left:0;top:0;width:932px;height:89px;background:linear-gradient(180deg,var(--header-top),var(--header-bottom))}
.brand{position:absolute;left:62px;top:30px;display:flex;align-items:center;gap:8px}
.brand-square{flex:none;width:26px;height:26px;background:var(--green)}
.brand-name{font-family:var(--display);font-weight:500;font-size:20px;letter-spacing:1px;color:var(--green-dark)}
.main-nav{position:absolute;right:62px;top:37px;display:flex;gap:22px;font-family:var(--serif);font-size:10.8px}
.main-nav a{color:#222;text-decoration:none}
.main-nav a.current{color:var(--green-dark)}

.hero-band{position:absolute;left:0;top:89px;width:932px;height:254px;background:linear-gradient(180deg,var(--wood-top),var(--wood-bottom))}
.hero-title{position:absolute;top:111px;width:932px;text-align:center;font-family:var(--serif);font-weight:400;font-size:26px;color:#333}
.hero-title .amp{color:var(--green-dark);text-decoration:underline;text-underline-offset:4px}

.slider{position:absolute;left:62px;top:173px;width:808px;height:275px;overflow:hidden}
.slide-photo{position:absolute;inset:0;background:linear-gradient(180deg,#3f5a36 0%,#4f6d3e 35%,#5d7b55 55%,#c9853e 78%,#e49a4d 100%)}
.slide-caption{position:absolute;left:0;top:174px}
.slide-caption h2{font-family:var(--display);font-weight:700;font-size:19px;line-height:22px;color:#fff;letter-spacing:-.3px}
.slide-caption h2 span{display:inline-block;background:var(--caption);padding:1px 14px 2px 14px}
.slide-caption p{margin:8px 0 0 14px;width:190px;font-family:var(--serif);font-style:italic;font-size:8.5px;line-height:10px;color:#3a2410}
.arrow{position:absolute;top:140px;width:12px;height:20px}

.rule{position:absolute;left:62px;width:808px;height:1px;background:var(--rule)}

.intro{position:absolute;left:179px;top:490px;font-family:var(--serif);font-size:21px;color:#333}
.intro b{color:var(--green-dark)}
.btn{position:absolute;display:flex;align-items:center;justify-content:center;background:var(--green);color:#fff;font-family:var(--serif);font-style:italic;font-size:13px}

.section-title{position:absolute;left:68px;font-family:var(--sans);font-weight:400;font-size:13.5px;color:#222}
.section-text{position:absolute;left:68px;width:180px;font-size:8px;line-height:12.5px;color:#333}
.pill{position:absolute;left:68px;height:14px;padding:0 18px 0 5px;background:#eee;border:1px solid #e2e2e2;font-family:var(--serif);font-size:8px;line-height:12px;color:#aaa}
.pill::after{content:"";position:absolute;right:6px;top:4px;border-left:4px solid #aaa;border-top:3px solid transparent;border-bottom:3px solid transparent}

.tile{position:absolute;width:187px;height:110px}
.tile-label{position:absolute;left:0;bottom:0;width:100%;height:14px;background:rgba(0,0,0,.65);color:#fff;font-size:7.5px;line-height:14px;padding-left:9px}
.ph-deck{background:linear-gradient(160deg,#b6b1a4,#8a7a66 55%,#3d4a3f)}
.ph-garden{background:linear-gradient(170deg,#8a9478,#5e7a4e 55%,#3f5c6a)}
.ph-modern{background:linear-gradient(170deg,#b7b85e,#8c9a5a 50%,#4d5b3a)}
.ph-path{background:linear-gradient(160deg,#7b6a3c,#5c6a3a 50%,#3a4a2c)}
.ph-falls{background:linear-gradient(90deg,#2f5a2a,#a9b8a8 50%,#2f5a2a)}

.story{position:absolute;width:190px}
.story-head{display:flex;gap:8px;font-size:10.5px;color:#222;line-height:13px}
.story-date{width:30px;font-size:10px}
.story-date small{display:flex;align-items:center;gap:3px;font-size:8px}
.bubble{display:inline-block;width:11px;height:8px;background:#333;border-radius:1px}
.story p{margin-top:8px;font-size:8px;line-height:12.5px;color:#333}
.more{position:absolute;font-family:var(--serif);font-size:8px;color:var(--link)}
.more.dim{color:#aaa}
.more::after{content:"";display:inline-block;margin-left:6px;border-left:4px solid currentColor;border-top:3px solid transparent;border-bottom:3px solid transparent}

.vdivider{position:absolute;left:683px;top:730px;width:1px;height:198px;background:var(--rule)}
.tweets{position:absolute;left:694px;top:726px;width:170px}
.tweets h3{font-family:var(--sans);font-weight:400;font-size:13px;color:#222;line-height:14px}
.tweets .via{font-size:7.5px;color:#333}
.follow{position:absolute;left:108px;top:6px;height:14px;padding:0 16px 0 5px;background:#eee;border:1px solid #e2e2e2;font-family:var(--serif);font-size:7.5px;line-height:12px;color:#aaa}
.follow::after{content:"";position:absolute;right:5px;top:4px;border-left:4px solid #aaa;border-top:3px solid transparent;border-bottom:3px solid transparent}
.tweet{margin-top:16px;font-size:8px;line-height:12.5px;color:#333}
.tweet a{color:var(--link);text-decoration:none}
.tweet small{display:block;font-size:6.5px;color:#aaa}

.cta-text{position:absolute;left:163px;top:980px;font-family:var(--serif);font-size:13px;line-height:17px;color:#333}

.site-footer{position:absolute;left:0;top:1078px;width:932px;height:122px;background:var(--footer)}
.fcol{position:absolute;top:14px}
.fcol h4{font-family:var(--sans);font-weight:600;font-size:10.5px;color:#333;letter-spacing:.3px;margin-bottom:8px}
.flinks{display:grid;grid-template-columns:77px 70px;font-size:8px;line-height:12.5px;color:#333}
.fcontact li{list-style:none;display:flex;align-items:flex-start;gap:9px;font-size:8px;line-height:10px;color:#333;margin-bottom:7px}
.fcontact svg{flex:none}
.newsletter p{width:170px;font-size:8px;line-height:12.5px;color:#333}
.signup{margin-top:6px;display:flex;width:146px;height:19px;background:#d4d4d4}
.signup span{flex:1;font-size:9px;line-height:19px;padding-left:8px;color:#333}
.signup b{width:26px;font-size:9px;line-height:19px;color:#333}
.newsletter small{display:block;margin-top:4px;font-size:6.5px;color:#999}
.fbrand{position:absolute;left:700px;top:20px;width:160px;text-align:center}
.fbrand .name{display:flex;align-items:center;justify-content:center;gap:7px;font-family:var(--display);font-weight:500;font-size:19px;letter-spacing:1px;color:#8a8a8a}
.fbrand .sq{flex:none;width:22px;height:22px;background:#9a9a9a}
.fbrand p{margin-top:14px;font-size:8px;line-height:12.5px;color:#333}
</style>
</head>
<body>

<header class="site-header">
  <div class="brand"><span class="brand-square"></span><span class="brand-name">GLIMMERSEAL</span></div>
  <nav class="main-nav">
    <a class="current" href="#">Home</a><a href="#">About Us</a><a href="#">Happenings</a><a href="#">Gallery</a><a href="#">Liner Styles</a><a href="#">Preparation</a><a href="#">Installation</a><a href="#">Contact Us</a>
  </nav>
</header>

<div class="hero-band" role="img" aria-label="Light timber plank background"></div>
<h1 class="hero-title">Custom made liners for ponds, pools <span class="amp">&amp;</span> watergardens.</h1>

<section class="slider">
  <div class="slide-photo" role="img" aria-label="Rock garden pond with waterfall, ferns, wooden ladder and timber deck in the foreground"></div>
  <svg class="arrow" style="left:8px" viewBox="0 0 12 20"><path d="M10 2 L3 10 L10 18" fill="none" stroke="rgba(255,255,255,.6)" stroke-width="2"/></svg>
  <svg class="arrow" style="right:8px" viewBox="0 0 12 20"><path d="M2 2 L9 10 L2 18" fill="none" stroke="rgba(255,255,255,.6)" stroke-width="2"/></svg>
  <div class="slide-caption">
    <h2><span>Vivamus hendre rhoncus felis ne</span><br><span>mauris imperdiet...</span></h2>
    <p>Nullam in dui mauris. Vivamus hendrerit arcu sed erat molestie vehicula. Sed auctor neque eu tellus rhoncus... (Read More)</p>
  </div>
</section>

<div class="rule" style="top:469px"></div>
<p class="intro">Read about <b>who</b> we are and <b>how</b> we work</p>
<a class="btn" style="left:646px;top:492px;width:86px;height:23px">About Us</a>
<div class="rule" style="top:542px"></div>

<h3 class="section-title" style="top:562px">Liner Styles</h3>
<p class="section-text" style="top:591px">Glimmerseal pond liners can be made to suit any size or shape pond...</p>
<span class="pill" style="top:663px">View all styles</span>
<div class="tile ph-deck" style="left:269px;top:567px" role="img" aria-label="Curved timber deck over a garden pond"><span class="tile-label">Flat Sheet Liners</span></div>
<div class="tile ph-garden" style="left:476px;top:567px" role="img" aria-label="Planted pond with rocks and grasses"><span class="tile-label">Composite Liners</span></div>
<div class="tile ph-modern" style="left:683px;top:567px" role="img" aria-label="Modern pond with stepping stones and water feature"><span class="tile-label">Profile Liners</span></div>

<div class="rule" style="top:705px"></div>

<h3 class="section-title" style="top:726px">Happenings</h3>
<p class="section-text" style="top:755px;width:185px">Lorem ipsum dolor sit amet, consectetur adipisicing elit, sed do eiusmod tempor incididunt ut labore et dolore magna aliqua.</p>
<span class="pill" style="top:829px">More stories</span>

<div class="tile ph-path" style="left:269px;top:729px" role="img" aria-label="Lit garden path leading to a cabin"></div>
<div class="story" style="left:272px;top:848px">
  <div class="story-head"><div class="story-date">16/05<small>42 <i class="bubble"></i></small></div><div>Lorem ipsum dolor sit ament, consectuetre elit</div></div>
  <p>Lorem ipsum dolor sit amet, consectetur adipisicing elit, sed do eiusmod tempor incididunt ut labore et dolore magna aliqua.</p>
</div>
<a class="more" style="left:272px;top:929px">read more</a>

<div class="tile ph-falls" style="left:476px;top:729px" role="img" aria-label="Small waterfall between ferns"></div>
<div class="story" style="left:479px;top:848px">
  <div class="story-head"><div class="story-date">15/05<small>12 <i class="bubble"></i></small></div><div>Lorem ipsum dolor sit ament, consectuetre elit</div></div>
  <p>Lorem ipsum dolor sit amet, consectetur adipisicing elit, sed do eiusmod tempor incididunt ut labore et dolore magna aliqua.</p>
</div>
<a class="more dim" style="left:479px;top:929px">read more</a>

<div class="vdivider"></div>
<aside class="tweets">
  <h3>Twitter</h3>
  <div class="via">via @glimmerseal</div>
  <span class="follow">follow us</span>
  <p class="tweet">Lorem ipsum dolor sit amet:<br><a href="#">http://lnk.to/qT7w3B</a><br>#glimmerseal<small>30 minutes ago</small></p>
  <p class="tweet">Lorem ipsum dolor sit amet, consectetur adip! <a href="#">http://www.glimmerseal.com</a><small>1 hour ago</small></p>
  <p class="tweet">Lorem ipsum dolor sit amet, consectetur adipisicing elit, ;)<small>2 days ago</small></p>
</aside>

<div class="rule" style="top:960px"></div>
<p class="cta-text">If you have any questions, or wish to discuss ways in which we can help,<br>please feel free to contact us at any time.</p>
<a class="btn" style="left:657px;top:985px;width:105px;height:23px">Contact Us</a>
<div class="rule" style="top:1036px"></div>

<footer class="site-footer">
  <div class="fcol" style="left:68px">
    <h4>Glimmerseal</h4>
    <div class="flinks"><span>Home</span><span>Preparation</span><span>About</span><span>Installation</span><span>Happenings</span><span>Gallery</span><span>Liner Styles</span><span>Contact Us</span></div>
  </div>
  <div class="fcol" style="left:271px">
    <h4>Contact Us</h4>
    <ul class="fcontact">
      <li><svg width="11" height="9" viewBox="0 0 11 9"><path d="M1 3 Q5.5 -1 10 3 L8.5 4.5 L7 3.5 L4 3.5 L2.5 4.5 Z M2 5 L9 5 L10 9 L1 9 Z" fill="#222"/></svg>1300 264 718</li>
      <li><svg width="11" height="8" viewBox="0 0 11 8"><rect x=".5" y=".5" width="10" height="7" fill="none" stroke="#222"/><path d="M.5 .5 L5.5 4.5 L10.5 .5" fill="none" stroke="#222"/></svg>info@glimmerseal.com</li>
      <li><svg width="11" height="11" viewBox="0 0 11 11"><path d="M5.5 0 A4 4 0 0 1 9.5 4 C9.5 7 5.5 11 5.5 11 C5.5 11 1.5 7 1.5 4 A4 4 0 0 1 5.5 0 Z" fill="#222"/><circle cx="5.5" cy="4" r="1.5" fill="#ececec"/></svg>Suite 27/B, Reedwater Lane<br>Fernvale 40316, AU</li>
    </ul>
  </div>
  <div class="fcol newsletter" style="left:477px">
    <h4>Newsletter</h4>
    <p>Lorem ipsum dolor sit amet, consectetur adipisicing elit, sed do .</p>
    <div class="signup"><span>email address...</span><b>OK</b></div>
    <small>Your e-mail is safe in private with us!</small>
  </div>
  <div class="fbrand">
    <div class="name"><span class="sq"></span>GLIMMERSEAL</div>
    <p>Copyright © 2013 | All Rights Reserved.<br>Read our terms.</p>
  </div>
</footer>

</body>
</html>
```